PebbleLoom screens tidy up

We would like advice on how to better present the following home page and overview pages.

The existing website is functional, but the pages don't appear professionals and pleasing to the eye. We would specifically like feedback on alignment and padding of icons and text to make the screen more appealing and polished.

We are following the willow design system.

1 page

Sans Serif
• IBM Plex, Poppins

```html
<!DOCTYPE html>
<html lang="en">
<head>
<meta charset="utf-8">
<title>PebbleLoom – Overview</title>
<link rel="stylesheet" href="https://fonts.googleapis.com/css2?family=IBM+Plex+Sans:wght@400;500;600;700&display=swap">
<style>
:root{
  --navy:#0b1447;
  --ink:#0d1640;
  --amber:#f9a825;
  --amber-soft:#fbb040;
  --canvas:#e0e0e0;
  --card:#f9f9f9;
  --white:#ffffff;
  --muted:#c9cde0;
}
*{box-sizing:border-box;margin:0;padding:0}
html,body{width:1200px;height:675px;overflow:hidden}
body{font-family:"IBM Plex Sans",sans-serif;background:var(--canvas);color:var(--ink);position:relative}
.sidebar{position:absolute;left:0;top:0;width:214px;height:675px;background:var(--navy);color:var(--white)}
.brand{position:absolute;left:19px;top:30px;display:flex;align-items:center;gap:9px}
.brand-dot{width:26px;height:26px;border-radius:50%;background:var(--amber)}
.brand-name{font-size:20px;font-weight:600;letter-spacing:-.3px}
.nav-item{position:absolute;left:20px;display:flex;align-items:center;gap:10px;font-size:11.3px;font-weight:500}
.nav-item svg{width:10px;height:10px;stroke:currentColor;fill:none;stroke-width:1.4}
.nav-item.strong{font-weight:700}
.badge{position:absolute;left:161px;top:129px;background:var(--amber);color:var(--white);font-size:10px;border-radius:9px;padding:1px 5px}
.divider{position:absolute;left:20px;top:195px;width:174px;border-top:1px dashed #4a5488}
.section-label{position:absolute;left:20px;top:214px;font-size:11.3px;font-weight:500}
.plus{position:absolute;left:184px;top:211px;font-size:14px;font-weight:400}
.active-bar{position:absolute;left:0;top:248px;width:3px;height:12px;background:var(--amber)}
.is-active{color:var(--amber)}
.caret{position:absolute;left:186px;width:0;height:0;border-left:3.5px solid transparent;border-right:3.5px solid transparent}
.caret.up{top:252px;border-bottom:4px solid var(--amber)}
.caret.down{top:426px;border-top:4px solid var(--white)}
.sub-item{position:absolute;left:40px;font-size:11.3px;font-weight:500}
.sidebar-art{position:absolute;left:0;top:540px;width:214px;height:135px;background:linear-gradient(to top,#f59a1f 0%,#e88a1a 45%,rgba(11,20,71,0) 100%)}
.main{position:absolute;left:245px;top:0;width:924px;height:675px}
.crumb{position:absolute;top:20px;font-size:9.4px;font-weight:600}
.title{position:absolute;top:33px;font-size:20px;font-weight:600}
.title-mark{position:absolute;left:1px;top:53px;width:12px;height:2px;background:var(--amber)}
.user{position:absolute;left:830px;top:14px;display:flex;align-items:center;gap:7px}
.avatar{width:27px;height:27px;border-radius:50%;border:2px solid var(--amber);position:relative;overflow:hidden;background:var(--white)}
.avatar::after{content:"";position:absolute;right:0;bottom:0;width:5px;height:5px;border-radius:50%;background:#3cc46b}
.user-small{font-size:8px;letter-spacing:.3px}
.user-name{font-size:10px;font-weight:700}
.heading{position:absolute;display:flex;align-items:center;gap:9px;font-size:12.5px;font-weight:600}
.heading svg{width:11px;height:11px;stroke:var(--ink);fill:none;stroke-width:1.3}
.card{position:absolute;background:var(--card);border-radius:6px;box-shadow:0 2px 4px rgba(0,0,0,.06)}
.campaign-card{left:0;top:101px;width:924px;height:79px}
.campaign-name{position:absolute;left:16px;top:12px;font-size:12.5px;font-weight:500}
.campaign-desc{position:absolute;left:16px;top:41px;font-size:11px}
.pill{position:absolute;left:784px;top:28px;width:125px;height:23px;border-radius:3px;background:var(--amber-soft);color:var(--white);font-size:10px;display:flex;align-items:center;justify-content:center;box-shadow:0 3px 6px rgba(0,0,0,.15)}
.org-card{left:0;top:224px;width:924px;height:101px}
.org-name{position:absolute;top:11px;font-size:12.5px;font-weight:500}
.org-meta{position:absolute;top:32px;font-size:9.5px}
.org-stat{position:absolute;top:44px;display:flex;align-items:center;gap:12px;font-size:34px;font-weight:700}
.org-stat svg{width:24px;height:24px;stroke:var(--ink);fill:none;stroke-width:1.4}
.files-card{left:0;top:368px;width:326px;height:149px}
.card-title{position:absolute;left:13px;top:10px;font-size:12.5px;font-weight:500}
.stat{position:absolute;top:44px;width:90px;text-align:center}
.stat-badge{width:58px;height:58px;margin:0 auto;border-radius:50%;background:var(--amber);display:flex;align-items:center;justify-content:center;font-size:30px;font-weight:700}
.stat-label{margin-top:12px;font-size:11.3px}
.resources-card{left:357px;top:369px;width:567px;height:148px;display:flex;align-items:center;justify-content:center;font-size:10px}
.alerts-card{left:0;top:562px;width:566px;height:102px;display:flex;align-items:center;justify-content:center;font-size:10px}
</style>
</head>
<body>
<aside class="sidebar">
  <div class="brand"><span class="brand-dot"></span><span class="brand-name">PebbleLoom</span></div>
  <div class="nav-item strong" style="top:95px"><svg viewBox="0 0 10 10"><path d="M1 5 5 1.5 9 5v4H1z"/></svg>Home</div>
  <div class="nav-item" style="top:129px"><svg viewBox="0 0 10 10"><path d="M2 7V4.5a3 3 0 0 1 6 0V7H2M4 8.5h2"/></svg>All Alerts</div>
  <span class="badge">3 new</span>
  <div class="nav-item" style="top:162px"><svg viewBox="0 0 10 10"><circle cx="5" cy="5" r="3.5"/><circle cx="5" cy="5" r="1.2"/></svg>Manage</div>
  <div class="divider"></div>
  <div class="section-label">Campaigns</div>
  <div class="plus">+</div>
  <div class="active-bar"></div>
  <div class="nav-item is-active" style="top:246px"><svg viewBox="0 0 10 10"><path d="M2 8 7.5 2.5l1 1L3 9H2zM1 9.5h8"/></svg>My Custom Campaigns</div>
  <span class="caret up"></span>
  <div class="sub-item is-active" style="top:276px">Overview</div>
  <div class="sub-item" style="top:304px">Files &amp; HoneyTokens</div>
  <div class="sub-item" style="top:331px">Resources</div>
  <div class="sub-item" style="top:359px">Alerts</div>
  <div class="sub-item" style="top:386px">Settings</div>
  <div class="nav-item" style="top:419px"><svg viewBox="0 0 10 10"><path d="M1 1v8h8M3 7V4M5 7V2M7 7V5"/></svg>Default Campaign</div>
  <span class="caret down"></span>
  <div class="sidebar-art" role="img" aria-label="Decorative amber honeycomb pattern"></div>
</aside>

<main class="main">
  <div class="crumb">My Custom Campaign</div>
  <h1 class="title">Overview</h1>
  <div class="title-mark"></div>
  <div class="user">
    <div class="avatar"></div>
    <div><div class="user-small">WELCOME</div><div class="user-name">Mara Elwood</div></div>
  </div>

  <div class="heading" style="left:0;top:75px"><svg viewBox="0 0 12 12"><path d="M1 4.5h2l6-3v9l-6-3H1zM3 7.5l1 3"/></svg>Campaigns</div>
  <section class="card campaign-card">
    <div class="campaign-name">My Custom Campaign</div>
    <div class="campaign-desc">This is my custom campaign for finding ...</div>
    <div class="pill">Custom</div>
  </section>

  <div class="heading" style="left:4px;top:199px"><svg viewBox="0 0 12 12"><path d="M1 11V1h6v10M7 4h4v7M3 3h2M3 5h2M3 7h2"/></svg><span style="margin-left:3px">Campaign Organization</span></div>
  <section class="card org-card">
    <div class="org-name" style="left:16px">Self-enabling&nbsp; Deliverables Proprietary Limited</div>
    <div class="org-meta" style="left:18px">Standard</div>
    <div class="org-stat" style="left:109px"><svg viewBox="0 0 24 24"><circle cx="7" cy="6" r="2.5"/><circle cx="17" cy="6" r="2.5"/><circle cx="12" cy="12" r="2.5"/><path d="M2 14a5 5 0 0 1 5-4M22 14a5 5 0 0 0-5-4M6 21a6 6 0 0 1 12 0"/></svg>86</div>
    <div class="org-name" style="left:594px">Unleash bleeding-edge mindshare</div>
    <div class="org-meta" style="left:594px">8 hours ago</div>
    <div class="org-stat" style="left:665px"><svg viewBox="0 0 24 24"><rect x="9" y="2" width="6" height="5"/><path d="M12 7v5M4 17v-5h16v5M12 12v5"/><circle cx="4" cy="19" r="2"/><circle cx="12" cy="19" r="2"/><circle cx="20" cy="19" r="2"/></svg>8</div>
  </section>

  <div class="heading" style="left:4px;top:344px"><svg viewBox="0 0 12 12"><path d="M3 3V1h6l2 2v7H9M1 3h6l2 2v6H1z"/></svg><span style="margin-left:3px">Files &amp; HoneyTokens</span></div>
  <div class="heading" style="left:358px;top:344px"><svg viewBox="0 0 12 12"><circle cx="6" cy="3" r="2"/><circle cx="3" cy="8" r="2"/><circle cx="9" cy="8" r="2"/></svg><span style="margin-left:3px">Resources</span></div>
  <section class="card files-card">
    <div class="card-title">Statistics</div>
    <div class="stat" style="left:47px"><div class="stat-badge">30</div><div class="stat-label">🗎 Files</div></div>
    <div class="stat" style="left:172px;width:120px;margin-left:-15px"><div class="stat-badge">0</div><div class="stat-label">○ HoneyTokens</div></div>
  </section>
  <section class="card resources-card">Generate a collection of fictional organizations, custom templates, uploaded files and logos</section>

  <div class="heading" style="left:0;top:537px"><svg viewBox="0 0 12 12"><path d="M2.5 8.5V5.5a3.5 3.5 0 0 1 7 0v3h-7M5 10.5h2"/></svg>Alerts</div>
  <section class="card alerts-card">Alert statistics will appear here</section>
</main>
</body>
</html>
```